依頼詳細
値段は入れず、『不安を安心に』『疑問を納得へ』『生活保護のご葬儀 自己負担0円』と言った文言を入れていただきたいです。
葬儀の流れの図も入れていただきたいです。
※添付ファイルを参照ください。
記載項目
電話番号のところは◯にしておいてください
サイズ
A4
ページ数
片面
希望イメージ
シンプル 複雑
単色 カラフル
暗い 明るい
日常 高級
遊び心 厳粛
未来的 伝統的
女性的 男性的
希望する色
赤系
納品ファイル
• 高解像度JPG (.jpg)
• イラストレーター形式 (.ai)
• フォトショップ形式 (.psd)
• PNG形式 (.png)
補足説明
■ 選んだ理由

シンプルで中身がわかりやすく気に入りました

■ 提案者全員のお礼・コメント

ありがとうございます!!また機会がありましたらお願い致します

```html
<!DOCTYPE html>
<html lang="ja">
<head>
<meta charset="utf-8">
<title>生活保護のご葬儀</title>
<link href="https://fonts.googleapis.com/css2?family=Shippori+Mincho:wght@500;700;800&family=Noto+Sans+JP:wght@400;500;700&display=swap" rel="stylesheet">
<style>
  :root{
    --ink:#3a3338;
    --pink:#e47d9d;
    --pink-deep:#c9577f;
    --mauve:#b86e9c;
    --mauve-light:#efdbe8;
    --card-bg:#fbf3f7;
    --band-a:#f2a6bd;
    --band-b:#e57c9e;
    --paper:#ffffff;
    --flower-a:#f6e6ec;
    --flower-b:#fdf8fa;
    --grey:#8d8d8d;
  }
  *{box-sizing:border-box;margin:0;padding:0}
  html,body{width:854px;height:1200px;overflow:hidden;background:var(--paper)}
  .page{position:relative;width:854px;height:1200px;overflow:hidden;background:var(--paper);
    font-family:"Noto Sans JP",sans-serif;color:var(--ink)}
  .flowers-top{position:absolute;left:0;top:0;width:854px;height:180px;
    background:linear-gradient(100deg,var(--paper) 0%,var(--flower-b) 35%,var(--flower-a) 100%)}
  .flowers-bottom{position:absolute;left:0;bottom:0;width:854px;height:300px;
    background:linear-gradient(180deg,rgba(255,255,255,0) 0%,var(--flower-a) 100%)}
  .headline{position:absolute;left:30px;top:28px;font-family:"Shippori Mincho",serif;font-weight:700;
    font-size:40px;line-height:1.6;color:var(--ink);letter-spacing:2px}
  .headline .line2{display:block;padding-left:40px}
  .cost-badge{position:absolute;left:588px;top:30px;width:240px;height:124px;background:var(--pink);
    color:#fff;text-align:center;font-family:"Shippori Mincho",serif;font-weight:800;padding-top:14px}
  .cost-badge .t1{font-size:27px;letter-spacing:1px}
  .cost-badge .t2{font-size:27px;margin-top:4px}
  .cost-badge .zero{font-size:54px;line-height:1;vertical-align:-6px}
  .section-band{position:absolute;left:56px;top:190px;width:742px;height:40px;
    background:linear-gradient(90deg,var(--band-a),var(--band-b),var(--band-a));
    color:#fff;font-family:"Shippori Mincho",serif;font-weight:700;font-size:24px;
    text-align:center;line-height:40px;letter-spacing:4px}
  .intro{position:absolute;left:96px;top:246px;width:680px;font-size:21px;line-height:1.95;letter-spacing:1px;font-weight:500}
  .pill{display:inline-block;background:var(--pink);color:#fff;font-size:15px;font-weight:700;
    padding:3px 26px;border-radius:20px}
  .target{position:absolute;left:36px;top:388px;width:300px}
  .target .pill{margin-left:70px;margin-bottom:16px}
  .target ul{list-style:none;font-size:13px;line-height:2.2}
  .target ul li::before{content:"■ ";color:var(--ink)}
  .target .note{font-size:13px;line-height:2;margin-top:8px}
  .plan{position:absolute;left:360px;top:388px;width:470px}
  .plan .pill{margin-left:150px;margin-bottom:12px}
  .vehicles{display:flex;gap:14px;height:92px}
  .vehicle{flex:1;background:linear-gradient(180deg,#e7e7e9,#bfc0c4);border-radius:4px}
  .items{display:flex;gap:8px;margin-top:12px}
  .item{flex:1;text-align:center;font-size:11px}
  .item .ph{height:54px;background:linear-gradient(180deg,#f2eef0,#d9d3d6);border:1px solid #e2dbe0;margin-bottom:4px}
  .flow-title{position:absolute;left:0;top:626px;width:854px;text-align:center;
    font-family:"Shippori Mincho",serif;font-weight:700;font-size:26px;color:var(--pink-deep);letter-spacing:3px}
  .flow-title svg{position:absolute;top:0}
  .row{position:absolute;left:30px;width:794px;display:flex;align-items:center;justify-content:space-between}
  .row.one{top:680px;flex-direction:row-reverse}
  .row.two{top:968px}
  .card{width:170px;background:var(--card-bg);border:2px solid var(--mauve-light);border-radius:8px;
    display:flex;flex-direction:row-reverse;padding:8px;gap:8px}
  .row.one .card{height:248px}
  .row.two .card{height:220px}
  .card .head{width:58px;background:var(--mauve);border-radius:4px;display:flex;flex-direction:column;align-items:center;padding-top:8px;color:#fff}
  .card .num{width:38px;height:38px;border-radius:50%;background:#fff;color:var(--mauve);
    font-family:"Shippori Mincho",serif;font-weight:800;font-size:24px;display:flex;align-items:center;justify-content:center}
  .card .title{writing-mode:vertical-rl;font-family:"Shippori Mincho",serif;font-weight:800;
    font-size:28px;letter-spacing:4px;margin-top:12px}
  .card .title.small{font-size:19px;letter-spacing:1px}
  .card .desc{flex:1;writing-mode:vertical-rl;font-size:12.5px;line-height:1.7;color:var(--ink);padding-top:4px}
  .arrow{width:30px;height:40px}
  .down{position:absolute;left:30px;top:934px;width:60px;height:32px}
</style>
</head>
<body>
<div class="page">
  <div class="flowers-top" role="img" aria-label="白と淡いピンクの花の写真"></div>
  <div class="flowers-bottom" role="img" aria-label="淡いピンクの花の写真"></div>

  <h1 class="headline">不安を安心に…<span class="line2">疑問を納得へ…</span></h1>

  <div class="cost-badge">
    <div class="t1">生活保護のご葬儀</div>
    <div class="t2">自己負担<span class="zero">0</span>円</div>
  </div>

  <h2 class="section-band">生活保護葬儀について</h2>

  <p class="intro">生活保護受給者の方は市区町村福祉事務所・社会福祉課に葬祭扶助の申請をすることにより施主様は自己負担なしで御葬儀（火葬式）を執り行うことができます。</p>

  <section class="target">
    <span class="pill">対象者</span>
    <ul>
      <li>生活保護受給者が亡くなられた場合</li>
      <li>生活保護受給者が喪主になった場合</li>
    </ul>
    <p class="note">※故人が生活保護の受給者であっても葬儀を行う施主様に資力がある場合は適用されません。</p>
  </section>

  <section class="plan">
    <span class="pill">含まれるプラン</span>
    <div class="vehicles">
      <div class="vehicle" role="img" aria-label="寝台車の写真"></div>
      <div class="vehicle" role="img" aria-label="霊柩車の写真"></div>
    </div>
    <div class="items">
      <div class="item"><div class="ph" role="img" aria-label="寝台車のイラスト"></div>寝台車</div>
      <div class="item"><div class="ph" role="img" aria-label="安置のイラスト"></div>ご安置</div>
      <div class="item"><div class="ph" role="img" aria-label="棺のイラスト"></div>棺一式</div>
      <div class="item"><div class="ph" role="img" aria-label="骨壺のイラスト"></div>骨壺</div>
      <div class="item"><div class="ph" role="img" aria-label="火葬のイラスト"></div>火葬料</div>
    </div>
  </section>

  <h2 class="flow-title">
    <svg style="left:270px" width="80" height="34" viewBox="0 0 80 34"><path d="M0 24 Q40 4 80 18" fill="none" stroke="var(--pink)" stroke-width="1.5"/></svg>
    葬儀の流れ
    <svg style="left:504px" width="80" height="34" viewBox="0 0 80 34"><path d="M0 18 Q40 4 80 24" fill="none" stroke="var(--pink)" stroke-width="1.5"/></svg>
  </h2>

  <div class="row one">
    <article class="card"><div class="head"><span class="num">1</span><span class="title">ご臨終</span></div>
      <p class="desc">病院・ご自宅等でご逝去された際は、まず当社へご連絡ください。24時間365日対応いたします。</p></article>
    <svg class="arrow" viewBox="0 0 30 40"><path d="M22 4 L8 20 L22 36" fill="none" stroke="var(--mauve)" stroke-width="5"/></svg>
    <article class="card"><div class="head"><span class="num">2</span><span class="title">お迎え</span></div>
      <p class="desc">ご連絡をいただき次第、寝台車でお迎えにあがり、ご指定の場所へお連れいたします。</p></article>
    <svg class="arrow" viewBox="0 0 30 40"><path d="M22 4 L8 20 L22 36" fill="none" stroke="var(--mauve)" stroke-width="5"/></svg>
    <article class="card"><div class="head"><span class="num">3</span><span class="title">ご安置</span></div>
      <p class="desc">ご遺体を安置所へご安置し、ドライアイス等で丁寧に処置いたします。</p></article>
    <svg class="arrow" viewBox="0 0 30 40"><path d="M22 4 L8 20 L22 36" fill="none" stroke="var(--mauve)" stroke-width="5"/></svg>
    <article class="card"><div class="head"><span class="num">4</span><span class="title">お打合せ</span></div>
      <p class="desc">ご葬儀の日程や内容について、担当者が丁寧にご説明いたします。</p></article>
  </div>

  <svg class="down" viewBox="0 0 60 32"><path d="M6 4 L30 26 L54 4" fill="none" stroke="var(--mauve)" stroke-width="6"/></svg>

  <div class="row two">
    <article class="card"><div class="head"><span class="num">5</span><span class="title">ご出棺・火葬</span></div>
      <p class="desc">お別れの後ご出棺となり、火葬場にて火葬を執り行います。</p></article>
    <svg class="arrow" viewBox="0 0 30 40"><path d="M8 4 L22 20 L8 36" fill="none" stroke="var(--mauve)" stroke-width="5"/></svg>
    <article class="card"><div class="head"><span class="num">6</span><span class="title">葬儀</span></div>
      <p class="desc">近親者の皆様でゆっくりとお別れのお時間をお過ごしください。</p></article>
    <svg class="arrow" viewBox="0 0 30 40"><path d="M8 4 L22 20 L8 36" fill="none" stroke="var(--mauve)" stroke-width="5"/></svg>
    <article class="card"><div class="head"><span class="num">7</span><span class="title">ご収骨</span></div>
      <p class="desc">火葬後、ご遺族様の手でご遺骨を骨壺へお納めいただきます。</p></article>
    <svg class="arrow" viewBox="0 0 30 40"><path d="M8 4 L22 20 L8 36" fill="none" stroke="var(--mauve)" stroke-width="5"/></svg>
    <article class="card"><div class="head"><span class="num">8</span><span class="title small">生活保護の申請手続き</span></div>
      <p class="desc">葬祭扶助の申請手続きは当社が代行いたしますのでご安心ください。</p></article>
  </div>
</div>
</body>
</html>
```